Brightfernrx website

We are a weight loss clinic and we need a website built. please look at these websites for content and style. Just need like 5 pages see samples. AI files of logo are not avail yet so use sample for place set

https://glowshiftstudio.com/
ortanvital.com
https://pinecrestclinicalbodybalance.com/
https://yourslimmingnook.com/
https://qrvskinstudio.com/treatments/weight-loss-injections/

Target Market(s)

Women

Industry/Entity Type

weight loss

Coding

Coded - Design and coding required

Number of Pages Required

5+ page

Requirements
Nice to have
• please make look like a medspa website

```html
<!DOCTYPE html>
<html lang="en">
<head>
<meta charset="utf-8">
<title>Brightfernrx — Pricing</title>
<link rel="stylesheet" href="https://fonts.googleapis.com/css2?family=Gilda+Display&family=Open+Sans:wght@300;400&display=swap">
<style>
:root{
  --bg:#f1f3f2;
  --ink:#2b5b45;
  --forest:#2f6450;
  --teal:#41b08f;
  --teal-dark:#33705c;
  --gold:#d4a03a;
  --bronze:#a37b3c;
  --mint:#d3ebe0;
  --white:#ffffff;
  --rule:#dcdcdc;
  --body:#3f5a4e;
}
*{box-sizing:border-box;margin:0;padding:0}
html,body{width:1200px;height:3213px;overflow:hidden;background:var(--bg)}
body{position:relative;font-family:"Open Sans",sans-serif;color:var(--ink)}
.abs{position:absolute}
.serif{font-family:"Gilda Display",serif;font-weight:400}

/* nav */
.site-nav{left:0;top:0;width:1200px;height:50px;background:var(--white);box-shadow:0 1px 3px rgba(0,0,0,.08);z-index:5}
.nav-link{top:18px;font-size:12px;color:var(--ink);letter-spacing:.3px;transform:translateX(-50%);white-space:nowrap}
.nav-link.active{color:var(--teal)}
.nav-link.cta{color:var(--gold)}
.brand{left:600px;top:12px;transform:translateX(-50%);display:flex;align-items:center;gap:7px;font-family:"Gilda Display",serif;font-size:20px;color:var(--teal-dark)}
.brand-dot{width:14px;height:14px;border-radius:50%;background:var(--teal)}

/* hero */
.hero-art{left:0;top:50px;width:1200px;height:450px;background:radial-gradient(ellipse 420px 230px at 600px 330px,#a9d6c9 0%,#cfe8de 55%,rgba(241,243,242,0) 100%),linear-gradient(180deg,#d3ebe0 0%,#e3f0ea 60%,var(--bg) 100%)}
.hero-title{left:0;top:248px;width:1200px;text-align:center;font-size:45px;line-height:52px;color:var(--ink)}

.section-title{left:0;width:1200px;text-align:center;font-size:34px;line-height:42px;color:var(--ink)}
.section-title.lg{font-size:37px;line-height:42px}

/* pricing */
.panel{width:442px;height:589px}
.panel.teal{background:linear-gradient(180deg,#1f6f5a 0%,#2f8e74 35%,var(--teal) 55%,var(--teal) 100%)}
.panel.deep{background:linear-gradient(180deg,#123f33 0%,#23584a 35%,var(--teal-dark) 55%,var(--teal-dark) 100%)}
.panel.bronze{background:linear-gradient(180deg,#6f5a2c 0%,#8d6e35 35%,var(--bronze) 55%,var(--bronze) 100%)}
.plan{width:329px;height:429px;background:var(--white);text-align:center;color:var(--ink)}
.plan.featured{background:var(--gold);color:var(--white)}
.plan-name{margin-top:33px;font-size:22px;line-height:26px}
.plan-price{margin-top:18px;font-size:41px;line-height:46px}
.plan-desc{margin:22px auto 0;width:226px;font-size:12px;line-height:21px;font-weight:300;color:var(--body)}
.plan.featured .plan-desc{color:var(--white)}
.plan-list{list-style:none;width:263px;margin:12px auto 0;font-size:12px;font-weight:300}
.plan-list li{padding:16px 0 17px;border-bottom:1px solid var(--rule);line-height:13px}
.plan.featured .plan-list li{border-bottom:2px solid var(--white)}
.plan-btn{position:absolute;left:0;bottom:0;width:100%;height:40px;line-height:40px;font-size:12px;font-weight:300;background:var(--gold);color:var(--white)}
.plan.featured .plan-btn{background:var(--white);color:var(--ink)}

/* accordion */
.faq{width:382px;border-left:2px solid #d9dfdc}
.faq-open{border-left:2px solid var(--gold);margin-left:-2px;padding:17px 0 17px 0;height:174px}
.faq-row{position:relative;padding-left:56px;font-size:12px;font-weight:300;color:var(--ink)}
.faq-num{position:absolute;left:20px;top:0}
.faq-sign{position:absolute;right:10px;top:-2px;font-size:14px;color:#9aa8a1}
.faq-open .faq-row{color:var(--gold)}
.faq-body{margin:20px 0 0 56px;width:326px;font-size:12px;line-height:21px;font-weight:300;color:var(--ink)}
.faq-item{height:54px;padding-top:25px}

/* footer */
.footer-fade{left:0;top:2632px;width:1200px;height:190px;background:linear-gradient(180deg,var(--bg) 0%,#cfe8de 60%,#bfe0d3 100%)}
.site-footer{left:0;top:2810px;width:1200px;height:403px;background:var(--forest)}
.footer-foliage{left:250px;top:2880px;width:700px;height:333px;background:radial-gradient(ellipse at center,rgba(80,140,110,.35) 0%,rgba(47,100,80,0) 70%)}
.footer-text{left:0;width:1200px;text-align:center;color:var(--white);font-family:"Gilda Display",serif}
.footer-rule{left:0;top:3143px;width:1200px;height:1px;background:rgba(255,255,255,.12)}
</style>
</head>
<body>

<header class="site-nav abs">
  <span class="nav-link abs" style="left:238px">HOME</span>
  <span class="nav-link abs" style="left:321px">SERVICES</span>
  <span class="nav-link abs active" style="left:417px">PRICING</span>
  <div class="brand abs"><span class="brand-dot"></span>Brightfernrx</div>
  <span class="nav-link abs" style="left:757px">ABOUT</span>
  <span class="nav-link abs" style="left:843px">CONTACT</span>
  <span class="nav-link abs cta" style="left:967px">BOOK ONLINE</span>
</header>

<div class="hero-art abs" role="img" aria-label="Soft mint lotus flower artwork"></div>
<h1 class="hero-title abs serif">The natural way of gaining<br>a perfect body &amp; mind</h1>

<h2 class="section-title abs serif" style="top:522px">Pay as you wish<br>monthly or yearly</h2>

<div class="panel teal abs" style="left:158px;top:650px" role="img" aria-label="Green leaves with water drops"></div>
<div class="panel deep abs" style="left:600px;top:650px" role="img" aria-label="Dense dark green foliage"></div>

<article class="plan abs" style="left:215px;top:726px">
  <h3 class="plan-name serif">Monthly</h3>
  <p class="plan-price serif">$45</p>
  <p class="plan-desc">Fusce ut velit laoreet, tempus arcu eu, molestie tortor. Nam vel justo cursus, faucibus lorem eget, egestas eros.</p>
  <ul class="plan-list"><li>Maecenas eleifend erat at</li><li>Justo fringilla imperdiet id ac magna.</li></ul>
  <div class="plan-btn">View more details</div>
</article>
<article class="plan abs" style="left:656px;top:726px">
  <h3 class="plan-name serif">Annual</h3>
  <p class="plan-price serif">$499</p>
  <p class="plan-desc">Fusce ut velit laoreet, tempus arcu eu, molestie tortor. Nam vel justo cursus, faucibus lorem eget, egestas eros.</p>
  <ul class="plan-list"><li>Maecenas eleifend erat at</li><li>Justo fringilla imperdiet id ac magna.</li></ul>
  <div class="plan-btn">View more details</div>
</article>

<h2 class="section-title abs serif" style="top:1342px">Premium and Group<br>membership plans</h2>

<div class="panel bronze abs" style="left:158px;top:1471px" role="img" aria-label="Golden toned leaves with water drops"></div>
<div class="panel deep abs" style="left:600px;top:1471px" role="img" aria-label="Dense dark green foliage"></div>

<article class="plan featured abs" style="left:215px;top:1547px">
  <h3 class="plan-name serif">PREMIUM</h3>
  <p class="plan-price serif">$45</p>
  <p class="plan-desc">Fusce ut velit laoreet, tempus arcu eu, molestie tortor. Nam vel justo cursus, faucibus lorem eget, egestas eros.</p>
  <ul class="plan-list"><li>Maecenas eleifend erat at</li><li>Justo fringilla imperdiet id ac magna.</li></ul>
  <div class="plan-btn">View more details</div>
</article>
<article class="plan abs" style="left:656px;top:1547px">
  <h3 class="plan-name serif">Annual</h3>
  <p class="plan-price serif">$499</p>
  <p class="plan-desc">Fusce ut velit laoreet, tempus arcu eu, molestie tortor. Nam vel justo cursus, faucibus lorem eget, egestas eros.</p>
  <ul class="plan-list"><li>Maecenas eleifend erat at</li><li>Justo fringilla imperdiet id ac magna.</li></ul>
  <div class="plan-btn">View more details</div>
</article>

<h2 class="section-title lg abs serif" style="top:2164px">Lorem ipsum dolor mit<br>samet et o mnia vanitare quantum</h2>

<div class="faq abs" style="left:181px;top:2293px">
  <div class="faq-open">
    <div class="faq-row"><span class="faq-num">1</span>Maecenas consectetur velit<span class="faq-sign">−</span></div>
    <p class="faq-body">Lorem ipsum dolor sit amet, consectetur adipiscing elit. Curabitur vel nisi tortor. Cras sollicitudin imperdiet tellus in interdum. Sed facilisis massa nec volutpat condimentum. In dui augue, rhoncus vitae nibh sodales, faucibus vehicula erat.</p>
  </div>
  <div class="faq-item"><div class="faq-row"><span class="faq-num">2</span>Cras sollicitudin<span class="faq-sign">+</span></div></div>
  <div class="faq-item"><div class="faq-row"><span class="faq-num">3</span>Sed facilisis massa nec volutpat<span class="faq-sign">+</span></div></div>
  <div class="faq-item"><div class="faq-row"><span class="faq-num">4</span>Lorem ipsum<span class="faq-sign">+</span></div></div>
</div>

<div class="faq abs" style="left:623px;top:2293px">
  <div class="faq-open">
    <div class="faq-row"><span class="faq-num">1</span>Maecenas consectetur velit<span class="faq-sign">−</span></div>
    <p class="faq-body">Lorem ipsum dolor sit amet, consectetur adipiscing elit. Curabitur vel nisi tortor. Cras sollicitudin imperdiet tellus in interdum. Sed facilisis massa nec volutpat condimentum. In dui augue, rhoncus vitae nibh sodales, faucibus vehicula erat.</p>
  </div>
  <div class="faq-item"><div class="faq-row"><span class="faq-num">2</span>Cras sollicitudin<span class="faq-sign">+</span></div></div>
  <div class="faq-item"><div class="faq-row"><span class="faq-num">3</span>Sed facilisis massa nec volutpat<span class="faq-sign">+</span></div></div>
  <div class="faq-item"><div class="faq-row"><span class="faq-num">4</span>Lorem ipsum<span class="faq-sign">+</span></div></div>
</div>

<div class="footer-fade abs" role="img" aria-label="Faint mint lotus petals"></div>
<footer class="site-footer abs"></footer>
<svg class="abs" style="left:0;top:0" width="1200" height="3213" aria-hidden="true">
  <path d="M470 2811 Q588 2806 600 2738 Q612 2806 730 2811 Z" fill="#2f6450"/>
</svg>
<div class="footer-foliage abs" role="img" aria-label="Tropical leaf pattern"></div>
<p class="footer-text abs" style="top:3015px;font-size:15px">Nullam viverra consectetuer quisque cursus et, porttitor risus.</p>
<p class="footer-text abs" style="top:3041px;font-size:13px">+00 (0) 4821 037 560 &nbsp;hello@fernclinic-mail.com</p>
<div class="footer-rule abs"></div>
<svg class="abs" style="left:1008px;top:3173px" width="14" height="9" aria-label="Back to top" role="img">
  <polyline points="1,8 7,2 13,8" fill="none" stroke="rgba(255,255,255,.5)" stroke-width="1.2"/>
</svg>

</body>
</html>
```